New Business needing a clean Information web site design to attract other business Users

Qavo Parcelback offers a returns handling service to on line selllers selling into Europe through marketplaces such as Trelloma, Vumo etc. We provide local addresses in various countries plus we handle the logistics of dealing with customer retrurns locally taking away the hassle of dealing with returns from the company and the end user.

We need a clean information site aimed at e commerce companies of various sizes who are our prospective customers.

The site contnet has been uploaded onto wordpress ready for design to be initiated.

Included in the design we are looking for a company logo too.
The site is currently located at
The web address will be
Regards
Dean Olafsen

Industry/Entity Type

Business

```html
<!DOCTYPE html>
<html lang="en">
<head>
<meta charset="utf-8">
<title>Qavo Parcelback – Returns Handling</title>
<link href="https://fonts.googleapis.com/css2?family=Open+Sans:wght@400;600;700;800&display=swap" rel="stylesheet">
<style>
:root{
  --orange:#f3a014;
  --orange-dark:#d98a06;
  --orange-soft:#f9c970;
  --ink:#333333;
  --muted:#777777;
  --light:#f1f1f1;
  --line:#dddddd;
  --footer:#1e1e1e;
  --white:#ffffff;
  --wood:#8a5a2e;
  --wood-light:#c89a64;
  --steel:#48576b;
}
*{box-sizing:border-box;margin:0;padding:0}
html,body{width:841px;height:1200px;overflow:hidden;background:var(--white)}
body{font-family:"Open Sans",Arial,sans-serif;color:var(--ink)}
.page{position:relative;width:841px;height:1200px;overflow:hidden}
.container{width:701px;margin:0 auto;position:relative}

/* header */
.site-header{height:90px;background:var(--white)}
.site-header .container{height:90px;display:flex;justify-content:space-between;align-items:center}
.brand{display:flex;align-items:center;gap:8px;font-weight:800;font-size:22px;letter-spacing:.5px;color:var(--orange);text-transform:uppercase}
.brand-dot{width:13px;height:13px;border-radius:50%;background:var(--orange)}
.header-tools{display:flex;flex-direction:column;align-items:flex-end;gap:10px}
.account-links{display:flex;gap:18px;font-size:8px;text-transform:uppercase;color:var(--muted);list-style:none}
.account-links li{display:flex;align-items:center;gap:4px}
.account-links li::before{content:"";width:7px;height:7px;border-radius:50%;background:var(--orange)}
.search{display:flex;border:1px solid var(--line);width:170px;height:22px}
.search span{flex:1;font-size:8px;color:#aaa;padding:5px 8px;text-transform:uppercase}
.search b{width:22px;display:flex;align-items:center;justify-content:center;border-left:1px solid var(--line)}

/* nav */
.main-nav{height:26px;background:var(--orange)}
.main-nav ul{list-style:none;display:flex;justify-content:space-between;height:26px;align-items:center}
.main-nav li{font-size:8.5px;font-weight:600;color:var(--white);text-transform:uppercase}

/* hero */
.hero{position:relative;height:416px;overflow:hidden}
.hero-photo{position:absolute;inset:0;background:
  linear-gradient(105deg,#3e2a18 0%,#6f4a28 22%,#a87848 42%,#d9cdb8 60%,#b9b1a6 76%,#5f5246 100%)}
.hero-shade{position:absolute;inset:0;background:linear-gradient(90deg,rgba(0,0,0,.4),rgba(0,0,0,0) 50%)}
.hero-text{position:absolute;left:70px;top:132px;width:300px;color:var(--white)}
.hero-text h1{font-size:25px;font-weight:700;letter-spacing:.5px;white-space:nowrap;margin-bottom:14px}
.hero-text p{font-size:7.5px;line-height:1.7;margin-bottom:22px}
.btn{display:inline-block;background:var(--orange);color:var(--white);font-size:8px;font-weight:700;text-transform:uppercase;padding:7px 14px}
.hero-arrow{position:absolute;top:200px}
.hero-arrow.prev{left:18px}
.hero-arrow.next{right:18px}

/* services */
.services{background:var(--light);height:146px;border-bottom:1px solid var(--line)}
.services ul{list-style:none;display:flex;justify-content:space-between;padding-top:24px}
.service{width:150px;text-align:center}
.service-art{width:64px;height:64px;margin:0 auto 16px;border-radius:50%;background:linear-gradient(145deg,var(--orange-soft),var(--orange) 60%,var(--orange-dark))}
.service h3{font-size:8px;font-weight:700;text-transform:uppercase;color:var(--ink)}

/* content */
.management{padding-top:44px;height:290px}
.management .container{display:flex;justify-content:space-between}
.management-text{width:395px}
.management-text h2{font-size:14px;font-weight:700;text-transform:uppercase;margin-bottom:16px}
.management-text p{font-size:7.5px;line-height:1.75;color:var(--muted);margin-bottom:11px}
.read-more{font-size:7.5px;color:var(--orange);font-weight:600}
.management-photo{width:286px;height:216px;background:
  linear-gradient(180deg,rgba(72,87,107,.85) 0%,rgba(72,87,107,.55) 45%,rgba(200,154,100,.9) 70%,var(--wood-light) 100%)}

/* newsletter */
.newsletter{background:var(--orange);height:74px}
.newsletter .container{display:flex;align-items:center;height:74px}
.newsletter-title{color:var(--white);text-transform:uppercase;width:215px}
.newsletter-title strong{display:block;font-size:17px;font-weight:700;line-height:1.1}
.newsletter-title span{font-size:9px}
.email-field{width:300px;height:24px;border:1px solid rgba(255,255,255,.8);font-size:7px;color:var(--white);padding:7px 10px;text-transform:uppercase}
.subscribe{margin-left:40px;background:#fbe3b4;color:#7a5300;font-size:9px;font-weight:700;text-transform:uppercase;padding:7px 16px}

/* footer */
.site-footer{background:var(--footer);height:158px;padding-top:24px;text-align:center;color:#cfcfcf}
.social{display:flex;justify-content:center;gap:12px;list-style:none;margin-bottom:16px}
.social li{width:14px;height:14px;background:#cfcfcf;border-radius:2px}
.footer-links{display:flex;justify-content:center;gap:12px;list-style:none;font-size:7.5px;margin-bottom:9px}
.footer-links li+li::before{content:"|";margin-right:12px;color:#777}
.copyright{font-size:7px;color:#999;margin-bottom:16px}
.payments{display:flex;justify-content:center;gap:7px;list-style:none}
.payments li{width:26px;height:16px;border-radius:2px;background:#e8e8e8}
.payments li:nth-child(2){background:#f0c040}
.payments li:nth-child(4){background:#d9534f}
.payments li:nth-child(6){background:#4a8fd0}
</style>
</head>
<body>
<div class="page">

  <header class="site-header">
    <div class="container">
      <div class="brand"><span class="brand-dot"></span>Qavo Parcelback</div>
      <div class="header-tools">
        <ul class="account-links">
          <li>My Account</li><li>Login</li><li>Register</li><li>Cart</li>
        </ul>
        <div class="search">
          <span>Search</span>
          <b><svg width="10" height="10" viewBox="0 0 10 10"><circle cx="4" cy="4" r="3" fill="none" stroke="#f3a014" stroke-width="1.4"/><line x1="6.3" y1="6.3" x2="9.3" y2="9.3" stroke="#f3a014" stroke-width="1.4"/></svg></b>
        </div>
      </div>
    </div>
  </header>

  <nav class="main-nav">
    <ul class="container">
      <li>Home</li><li>About Us</li><li>Why Online</li><li>Fulfillment Services</li><li>Shipping &amp; Returns</li><li>Contact Us</li>
    </ul>
  </nav>

  <section class="hero">
    <div class="hero-photo" role="img" aria-label="Photo of hands holding a smartphone showing an online shop page, warehouse shelves behind"></div>
    <div class="hero-shade"></div>
    <div class="hero-text">
      <h1>RETURNS HANDLING</h1>
      <p>We collect, inspect and restock your marketplace returns across Europe, giving shoppers a local address and giving your team more time to sell. Fast refunds, clear reports and careful handling come standard with every parcel we receive.</p>
      <span class="btn">Read More</span>
    </div>
    <svg class="hero-arrow prev" width="10" height="16" viewBox="0 0 10 16"><polyline points="8,1 2,8 8,15" fill="none" stroke="#fff" stroke-width="2.5"/></svg>
    <svg class="hero-arrow next" width="10" height="16" viewBox="0 0 10 16"><polyline points="2,1 8,8 2,15" fill="none" stroke="#fff" stroke-width="2.5"/></svg>
  </section>

  <section class="services">
    <ul class="container">
      <li class="service"><div class="service-art" role="img" aria-label="Illustration of stacked boxes on a pallet"></div><h3>Warehousing</h3></li>
      <li class="service"><div class="service-art" role="img" aria-label="Illustration of a figure carrying a parcel"></div><h3>Shipping</h3></li>
      <li class="service"><div class="service-art" role="img" aria-label="Illustration of a figure delivering a package at a door"></div><h3>Deliver Products</h3></li>
      <li class="service"><div class="service-art" role="img" aria-label="Illustration of two figures handing back a parcel"></div><h3>Returns Handling</h3></li>
    </ul>
  </section>

  <section class="management">
    <div class="container">
      <div class="management-text">
        <h2>Returns Handling Management</h2>
        <p>Selling into Europe through online marketplaces brings returns from many countries. We give each of your stores a local return address, so customers send items back quickly and cheaply, without long international postage or confusing paperwork at the counter.</p>
        <p>Every parcel is checked on arrival, graded and photographed. Sellable stock is repacked and held for you, while damaged goods are reported with clear notes for your records.</p>
        <p>Our team handles the questions, the logistics and the follow up, taking the hassle away from you and your buyers alike.</p>
        <span class="read-more">Read more &gt;&gt;</span>
      </div>
      <div class="management-photo" role="img" aria-label="Photo of a warehouse manager with a clipboard among cardboard boxes"></div>
    </div>
  </section>

  <section class="newsletter">
    <div class="container">
      <div class="newsletter-title"><strong>Newsletter</strong><span>Subscription</span></div>
      <div class="email-field">Email Address</div>
      <span class="subscribe">Subscribe</span>
    </div>
  </section>

  <footer class="site-footer">
    <ul class="social"><li></li><li></li><li></li><li></li></ul>
    <ul class="footer-links">
      <li>Home</li><li>About Us</li><li>Buy Online</li><li>Fulfillment Services</li><li>Shipping &amp; Returns</li><li>Contact Us</li>
    </ul>
    <p class="copyright">Copyright © 2015 Qavo Parcelback. All rights reserved.</p>
    <ul class="payments"><li></li><li></li><li></li><li></li><li></li><li></li></ul>
  </footer>

</div>
</body>
</html>
```